Tarjetas de visita para empresa de aluminio

Empresa con mas de 40 años vendiendo perfiles de aluminio.
Somos fábrica y almacén, queremos renovar la tarjeta de presentación de nuestros comerciales dando una imgen innovadora y tecnógica mezclado con la calidez del respeto al medio ambiente.
Añado el logo de la empresa y actual cara trasera de la tarjeta de visita, el logo es el simbolo WM y la marca TRAVENIC EXTRUSION, la frase 2extrusion y lacado de aluminio" debe cambiarse por "Diseño, extrusión, lacado, anodizado y mecanizado de precisión de aluminio" o en su defecto incluir todos esos servicios que hacemos o una frase mas pegadiza.

We are an aluminium factory, we produce and stock profiles of aluminium.
we want to renew visit card of our sellers, we are looking for something that show innovation, tecnology and environment respect.
Upload our actual logo and back of visit card, logo WM and brand TRAVENIC EXTRUSION must be keept.
Text "Extrusion y lacado de aluminio" must be changed for "Diseño, extrusion, lacado, anodizado y mecanizado de precisión de aluminio" or something like that

```html
<!DOCTYPE html>
<html lang="es">
<head>
<meta charset="utf-8">
<title>Travenic Extrusion – Tarjetas de visita</title>
<link href="https://fonts.googleapis.com/css2?family=Open+Sans:wght@400;600;700&display=swap" rel="stylesheet">
<style>
  :root {
    --bg: #ece6df;
    --card-black: #0b0b0c;
    --band-grey: #2a2b2d;
    --silver: #d6d8db;
    --silver-light: #f4f5f6;
    --paper: #eef0f1;
    --accent-blue: #1d8fc7;
    --ink: #2b2d30;
    --ink-soft: #5d6166;
  }
  * { box-sizing: border-box; margin: 0; padding: 0; }
  html, body { width: 1200px; height: 800px; overflow: hidden; }
  body {
    background: var(--bg);
    font-family: "Open Sans", Arial, sans-serif;
    position: relative;
  }
  .card {
    position: absolute;
    top: 250px;
    width: 510px;
    height: 300px;
    border-radius: 26px;
    overflow: hidden;
    box-shadow: 0 10px 28px rgba(60, 45, 30, 0.18);
  }
  .card-band { position: absolute; inset: 0; width: 100%; height: 100%; }

  /* Contact side */
  .card--contact {
    left: 60px;
    background: linear-gradient(135deg, var(--silver-light), var(--paper) 55%, #dfe2e4);
  }
  .contact-brand {
    position: absolute;
    top: 44px;
    right: 44px;
    display: flex;
    align-items: center;
    gap: 10px;
    color: var(--ink);
    font-weight: 600;
    font-size: 15px;
    letter-spacing: 2px;
  }
  .brand-dot {
    width: 26px; height: 26px;
    border-radius: 50%;
    border: 2px solid var(--ink);
  }
  .contact-emblem {
    position: absolute;
    left: 150px; top: 70px;
    width: 150px; height: 92px;
    border-radius: 50%;
    border: 3px solid #cfd2d5;
  }
  .contact-person {
    position: absolute;
    left: 150px;
    top: 176px;
    font-size: 12.5px;
    line-height: 1.42;
    color: var(--ink-soft);
  }
  .person-name { font-weight: 700; color: var(--ink); font-size: 14px; }
  .person-role { font-weight: 600; color: var(--accent-blue); font-size: 14px; }
  .contact-phones {
    position: absolute;
    right: 44px;
    top: 176px;
    font-size: 12.5px;
    line-height: 1.42;
    color: var(--ink-soft);
    text-align: left;
  }

  /* Brand side */
  .card--brand {
    left: 630px;
    background: var(--card-black);
  }
  .brand-lockup {
    position: absolute;
    left: 0; right: 90px;
    top: 70px;
    display: flex;
    flex-direction: column;
    align-items: center;
  }
  .brand-mark {
    width: 96px; height: 62px;
    border-radius: 50%;
    border: 3px solid var(--silver);
    margin-bottom: 18px;
  }
  .brand-name {
    color: var(--silver);
    font-weight: 600;
    font-size: 27px;
    letter-spacing: 4px;
    white-space: nowrap;
  }
  .brand-tagline {
    margin-top: 8px;
    color: #9a9da1;
    font-size: 9px;
    letter-spacing: 0.2px;
    white-space: nowrap;
  }
</style>
</head>
<body>

  <section class="card card--contact" aria-label="Tarjeta, cara de contacto">
    <svg class="card-band" viewBox="0 0 510 300" aria-hidden="true">
      <path d="M0 0 H62 C80 90 95 200 128 300 H0 Z" fill="var(--card-black)"/>
      <path d="M62 0 C80 90 95 200 128 300 H134 C101 200 86 90 68 0 Z" fill="var(--silver)"/>
      <path d="M68 0 C86 90 101 200 134 300 H138 C105 200 90 90 72 0 Z" fill="var(--accent-blue)"/>
    </svg>
    <div class="contact-emblem" aria-hidden="true"></div>
    <div class="contact-brand"><span class="brand-dot"></span>TRAVENIC EXTRUSION</div>
    <div class="contact-person">
      <p class="person-name">Marcos Ortega Ruiz</p>
      <p class="person-role">Comercial</p>
      <p>marcosortega@travenic.com</p>
      <p>Pol. Ind. Las Vegas - C/ 3 Nº 22</p>
      <p>41620 Villanueva del Río (Sevilla)</p>
      <p>Apartado de Correos 452</p>
    </div>
    <div class="contact-phones">
      <p>Tel: 954 71 28 40</p>
      <p>Fax: 954 71 28 41</p>
    </div>
  </section>

  <section class="card card--brand" aria-label="Tarjeta, cara de marca">
    <svg class="card-band" viewBox="0 0 510 300" aria-hidden="true">
      <path d="M398 0 C420 100 438 200 450 300 H510 V0 Z" fill="var(--band-grey)"/>
      <path d="M386 0 C408 100 426 200 438 300 H450 C438 200 420 100 398 0 Z" fill="var(--silver)"/>
      <path d="M380 0 C402 100 420 200 432 300 H438 C426 200 408 100 386 0 Z" fill="var(--accent-blue)"/>
    </svg>
    <div class="brand-lockup">
      <div class="brand-mark" aria-hidden="true"></div>
      <p class="brand-name">TRAVENIC EXTRUSION</p>
      <p class="brand-tagline">Diseño, extrusión, lacado, anodizado y mecanizado de precisión de aluminio</p>
    </div>
  </section>

</body>
</html>
```